Gymnastics Award Design Needed--for kids

Need a gymnastics certificate or award designed. Will be printed on a piece of 8.5x11 paper. The award will be celebrating the gymnast learning a new skill in gymnastics. So it should be fun, but still look "official". Needs to look good hanging on a gymnast's bedroom wall.

It should say "The Aerial Cartwheel Club"
I will be using this design to change it based on the skill.

My main colors are:
#34475D
#E1467A
#7555A4

So should use those, but can add others

My website is tumblenestpro.com so you can see the look/feel.

Target Market(s)

Main audience will be girls ages 5-12, but will also be used by slightly older girls and boys. So needs to be fun, not too gender specific.

Industry/Entity Type

Learning

Requirements
Must have
• The following will need to go on the certificate:
• * Name of Skill
• * Image of Skill
• * Gymnast's Name
• * my logo
• * Gym's Logo
• * Gym's Name
• Optional: Date

```html
<!DOCTYPE html>
<html lang="en">
<head>
<meta charset="utf-8">
<title>The Aerial Cartwheel Club – Certificate</title>
<link rel="stylesheet" href="https://fonts.googleapis.com/css2?family=League+Gothic&family=Yanone+Kaffeesatz:wght@300;400&family=Raleway:wght@300;400&family=Great+Vibes&display=swap">
<style>
  :root {
    --frame-pink: #e0457a;
    --accent-pink: #e1467a;
    --royal-purple: #68449c;
    --brand-purple: #7555a4;
    --paper: #ffffff;
    --rule-soft: #e9dff2;
    --leotard-gold: #f8b64c;
    --leotard-blue: #3aa9dc;
    --skin: #f4c3a4;
  }
  html, body {
    margin: 0;
    padding: 0;
    overflow: hidden;
    background: var(--frame-pink);
  }
  .certificate {
    position: relative;
    width: 1200px;
    height: 848px;
    overflow: hidden;
    background: var(--frame-pink);
  }
  .certificate__frame {
    position: absolute;
    inset: 0;
  }
  .club-name {
    position: absolute;
    top: 34px;
    left: 0;
    width: 100%;
    text-align: center;
    margin: 0;
    font-family: "Yanone Kaffeesatz", sans-serif;
    font-weight: 300;
    font-size: 66px;
    line-height: 1;
    color: var(--accent-pink);
    white-space: nowrap;
  }
  .club-name span {
    display: inline-block;
    transform: scaleX(0.62);
    transform-origin: center;
  }
  .title {
    position: absolute;
    top: 42px;
    left: 0;
    width: 100%;
    text-align: center;
    margin: 0;
    font-family: "League Gothic", sans-serif;
    font-weight: 400;
    color: var(--royal-purple);
    line-height: 1;
    white-space: nowrap;
  }
  .title__word {
    display: inline-block;
    font-size: 226px;
    transform: scaleX(0.68);
    transform-origin: center;
    letter-spacing: 2px;
  }
  .title__initial {
    font-size: 264px;
  }
  .presented-to {
    position: absolute;
    top: 300px;
    left: 0;
    width: 100%;
    text-align: center;
    margin: 0;
    font-family: "Raleway", sans-serif;
    font-weight: 400;
    font-size: 30px;
    letter-spacing: -1px;
    color: var(--royal-purple);
  }
  .name-line {
    position: absolute;
    top: 410px;
    left: 424px;
    width: 352px;
    height: 0;
    border-top: 1px solid var(--rule-soft);
  }
  .presenter {
    position: absolute;
    top: 458px;
    left: 404px;
    width: 392px;
    text-align: center;
    margin: 0;
    font-family: "Yanone Kaffeesatz", sans-serif;
    font-weight: 400;
    font-size: 56px;
    line-height: 1;
    color: var(--accent-pink);
    font-variant: small-caps;
    white-space: nowrap;
  }
  .presenter__rule {
    position: absolute;
    top: 516px;
    left: 424px;
    width: 352px;
    height: 0;
    border-top: 2px solid var(--accent-pink);
  }
  .signature {
    position: absolute;
    top: 528px;
    left: -16px;
    width: 100%;
    text-align: center;
    margin: 0;
    font-family: "Great Vibes", cursive;
    font-size: 62px;
    line-height: 1.2;
    color: var(--brand-purple);
  }
  .ribbon {
    position: absolute;
    top: 104px;
    width: 68px;
    height: 120px;
    background: var(--accent-pink);
    border-radius: 34px 34px 4px 4px;
  }
  .ribbon--left { left: 96px; }
  .ribbon--right { left: 1032px; }
  .gymnast {
    position: absolute;
    border-radius: 40px;
  }
  .gymnast--handstand {
    left: 92px;
    top: 420px;
    width: 228px;
    height: 296px;
    background: linear-gradient(160deg, var(--skin) 0%, var(--leotard-gold) 60%, #f2a93b 100%);
  }
  .gymnast--leap {
    left: 772px;
    top: 508px;
    width: 372px;
    height: 180px;
    background: linear-gradient(100deg, var(--skin) 0%, var(--leotard-blue) 50%, var(--skin) 100%);
  }
  .brand {
    position: absolute;
    top: 738px;
    left: 0;
    width: 100%;
    display: flex;
    justify-content: center;
    align-items: center;
    gap: 14px;
  }
  .brand__mark {
    width: 40px;
    height: 40px;
    border-radius: 50%;
    background: var(--brand-purple);
  }
  .brand__name {
    font-family: "Raleway", sans-serif;
    font-weight: 300;
    font-size: 44px;
    line-height: 1.1;
    color: var(--accent-pink);
    letter-spacing: 1px;
  }
</style>
</head>
<body>
<main class="certificate">
  <svg class="certificate__frame" width="1200" height="848" viewBox="0 0 1200 848" aria-hidden="true">
    <path fill="var(--paper)" d="M138 22 H1062 A104 74 0 0 0 1164 94 V752 A104 74 0 0 0 1062 826 H138 A104 74 0 0 0 36 752 V94 A104 74 0 0 0 138 22 Z"/>
  </svg>

  <div class="ribbon ribbon--left" role="img" aria-label="Pink awareness ribbon decoration"></div>
  <div class="ribbon ribbon--right" role="img" aria-label="Pink awareness ribbon decoration"></div>

  <p class="club-name"><span>THE AERIAL CARTWHEEL CLUB</span></p>
  <h1 class="title"><span class="title__word"><span class="title__initial">C</span>ERTIFICATE</span></h1>
  <p class="presented-to">Presented to :</p>
  <div class="name-line" aria-hidden="true"></div>

  <p class="presenter">By Maren TumbleNest Pro</p>
  <div class="presenter__rule" aria-hidden="true"></div>
  <p class="signature">signature</p>

  <div class="gymnast gymnast--handstand" role="img" aria-label="Illustration of a gymnast in a yellow leotard doing an aerial cartwheel"></div>
  <div class="gymnast gymnast--leap" role="img" aria-label="Illustration of a gymnast in a blue leotard doing a split leap"></div>

  <div class="brand">
    <span class="brand__mark" aria-hidden="true"></span>
    <span class="brand__name">TumbleNest Pro</span>
  </div>
</main>
</body>
</html>
```